Emergency Management Consulting Flyer

Company name: Stone Harbor Emergency Management

I am looking for a postcard design for my emergency management consulting business. I'm looking for something that has some colors and is double sided, on side with the information on services provided and the other side with the contact information. For the main side I'm looking for the following:

How prepared are you?

Services Provided:
Healthcare Preparedness
EOC Support
Emergency Planning
Mitigation Planning
Business Continuity
Disaster Response
Training and Exercises
Project Management
And more

Affordable for small and large organizations
Stand-by contracts available

On the back side, I'm looking for Contact Us section.

Overall I'm looking for something a bit more modern and need to have at least one disaster photo. If you have questions please message me.

Target Market(s)

Government, Healthcare Facilities, Businesses

Industry/Entity Type

Consulting

Requirements
Must have
• Disaster Picture, modern looking
• For the main side I'm looking for the following:
• How prepared are you?
• Services Provided:
• Healthcare Preparedness
• EOC Support
• Emergency Planning
• Mitigation Planning
• Business Continuity
• Disaster Response
• Training and Exercises
• Project Management
• And more
• Affordable for small and large organizations
• Stand-by contracts available

```html
<!DOCTYPE html>
<html lang="en">
<head>
<meta charset="utf-8">
<title>Stone Harbor Emergency Management – Postcard</title>
<link rel="stylesheet" href="https://fonts.googleapis.com/css2?family=Anton&family=Raleway:wght@400;600;700&display=swap">
<style>
  :root{
    --page:#ece8e1;
    --paper:#ffffff;
    --ink:#3a3a3c;
    --orange:#f07b2a;
    --orange-deep:#e2661b;
    --bar:#232223;
    --list-ink:#4a4a4c;
    --veil:rgba(246,246,244,.82);
  }
  *{box-sizing:border-box;margin:0;padding:0}
  html,body{width:1200px;height:729px;overflow:hidden;background:var(--page)}
  body{position:relative;font-family:"Raleway",Arial,sans-serif;color:var(--ink)}

  .card{position:absolute;overflow:hidden}

  /* ---------- mailing side ---------- */
  .card--mailer{left:58px;top:48px;width:572px;height:455px;background:var(--paper)}
  .mailer-panel{position:absolute;left:4px;top:8px;width:290px;height:380px;overflow:hidden}
  .mailer-photo{position:absolute;inset:0;background:linear-gradient(180deg,#d9dcd9 0%,#cfcac3 45%,#e4e1dc 75%,#efedea 100%)}
  .brand{position:absolute;display:flex;align-items:center;gap:7px}
  .brand-dot{width:22px;height:22px;border-radius:50%;background:var(--orange);flex:none}
  .brand-name{font-family:"Raleway",Arial,sans-serif;font-weight:700;color:var(--ink);text-transform:uppercase;line-height:1.05}
  .mailer-panel .brand{left:14px;top:28px}
  .mailer-panel .brand-name{font-size:15px;letter-spacing:.5px}
  .mailer-headline{position:absolute;left:14px;top:152px;font-family:"Anton",Impact,sans-serif;font-size:43px;line-height:1.02;color:#151515;text-transform:uppercase}
  .mailer-headline .accent{color:var(--orange)}
  .tab{position:absolute;background:var(--orange);color:#fff;font-weight:700;white-space:nowrap;border-radius:0 14px 0 0}
  .mailer-panel .tab{left:0;top:326px;height:18px;padding:0 14px 0 16px;font-size:10.5px;line-height:18px}
  .mailer-bar{position:absolute;left:0;top:344px;width:100%;height:36px;background:var(--bar)}

  /* ---------- services side ---------- */
  .card--front{left:597px;top:236px;width:573px;height:444px;background:var(--paper)}
  .front-photo-scene{position:absolute;left:0;top:0;width:300px;height:376px;background:linear-gradient(160deg,#c9cfd4 0%,#b9b4ad 55%,#8e8a86 100%)}
  .front-photo-scene::after{content:"";position:absolute;inset:0;background:var(--veil)}
  .front-photo-vehicle{position:absolute;left:300px;top:0;width:273px;height:376px;background:linear-gradient(180deg,#6f9cc6 0%,#a9c4d9 38%,#c9c0a2 58%,#55575a 80%,#3f4144 100%)}
  .card--front .brand{left:28px;top:24px}
  .card--front .brand-name{font-size:17px;letter-spacing:.6px}

  .services{position:absolute;left:28px;top:98px}
  .services-title{font-family:"Raleway",Arial,sans-serif;font-weight:600;font-size:22px;color:var(--ink);text-transform:uppercase;letter-spacing:.2px}
  .services-title .accent{color:var(--orange);font-weight:700}
  .services-list{list-style:none;margin-top:6px;position:relative}
  .services-list::before{content:"";position:absolute;left:0;top:0;width:20px;height:100%;background:var(--orange)}
  .service{position:relative;height:25.6px;display:flex;align-items:center;font-size:13px;color:var(--list-ink);text-transform:uppercase;letter-spacing:.3px}
  .service svg{position:relative;width:20px;height:14px;margin-right:7px;flex:none}

  .card--front .tab{left:0;top:352px;height:24px;padding:0 18px 0 26px;font-size:12.5px;line-height:24px;width:328px}
  .front-bar{position:absolute;left:0;top:376px;width:100%;height:68px;background:var(--bar);display:flex;align-items:center;padding-left:36px}
  .front-headline{font-family:"Anton",Impact,sans-serif;font-size:36px;color:#fff;text-transform:uppercase;letter-spacing:.3px}
  .front-headline .accent{color:var(--orange)}
  .standby{margin-left:20px;font-size:11.5px;line-height:1.12;color:#fff;text-transform:uppercase;letter-spacing:.5px}
  .standby .accent{color:var(--orange);font-weight:700}
</style>
</head>
<body>

<section class="card card--mailer" aria-label="Postcard mailing side">
  <div class="mailer-panel">
    <div class="mailer-photo" role="img" aria-label="Photo of a man standing before a house destroyed by a storm, fallen trees around it"></div>
    <div class="brand">
      <span class="brand-dot"></span>
      <span class="brand-name">Stone Harbor<br>Emergency Management</span>
    </div>
    <h2 class="mailer-headline">How<br><span class="accent">Prepared</span><br>Are You?</h2>
    <p class="tab">Affordable for small and large organizations</p>
    <div class="mailer-bar"></div>
  </div>
</section>

<section class="card card--front" aria-label="Postcard services side">
  <div class="front-photo-scene" role="img" aria-label="Photo of a paramedic wheeling a stretcher, softly blurred"></div>
  <div class="front-photo-vehicle" role="img" aria-label="Photo of an ambulance with rear doors open on a road under blue sky"></div>

  <div class="brand">
    <span class="brand-dot"></span>
    <span class="brand-name">Stone Harbor<br>Emergency Management</span>
  </div>

  <div class="services">
    <h2 class="services-title"><span class="accent">Services</span> Provided:</h2>
    <ul class="services-list">
      <li class="service"><svg viewBox="0 0 20 14"><circle cx="10" cy="7" r="5" fill="none" stroke="#fff" stroke-width="1.2"/><path d="M10 4.5v5M7.5 7h5" stroke="#fff" stroke-width="1.3"/></svg>Healthcare Preparedness</li>
      <li class="service"><svg viewBox="0 0 20 14"><path d="M10 2l4.5 1.8v3.4c0 2.6-2 4.2-4.5 4.9-2.5-.7-4.5-2.3-4.5-4.9V3.8z" fill="none" stroke="#fff" stroke-width="1.2"/></svg>EOC Support</li>
      <li class="service"><svg viewBox="0 0 20 14"><path d="M10 2l5 9.5H5z" fill="none" stroke="#fff" stroke-width="1.2"/><path d="M10 5.5v3M10 9.6v.8" stroke="#fff" stroke-width="1.2"/></svg>Emergency Planning</li>
      <li class="service"><svg viewBox="0 0 20 14"><circle cx="10" cy="3" r="1.6" fill="#fff"/><path d="M10 5v4l-2.5 3.5M10 9l2.5 3.5M7.5 7h5" stroke="#fff" stroke-width="1.3" fill="none"/></svg>Mitigation Planning</li>
      <li class="service"><svg viewBox="0 0 20 14"><rect x="5" y="4.5" width="10" height="7" rx="1" fill="none" stroke="#fff" stroke-width="1.2"/><path d="M8 4.5V3h4v1.5M5 7.5h10" stroke="#fff" stroke-width="1.2" fill="none"/></svg>Business Continuity</li>
      <li class="service"><svg viewBox="0 0 20 14"><circle cx="10" cy="2.8" r="1.6" fill="#fff"/><path d="M10 5v7M7 7.5h6" stroke="#fff" stroke-width="1.4"/></svg>Disaster Response</li>
      <li class="service"><svg viewBox="0 0 20 14"><rect x="9" y="2" width="6" height="4" fill="none" stroke="#fff" stroke-width="1.1"/><circle cx="6.5" cy="4" r="1.4" fill="#fff"/><path d="M6.5 6v6M6.5 7.5l3-1.5" stroke="#fff" stroke-width="1.3"/></svg>Training and Exercises</li>
      <li class="service"><svg viewBox="0 0 20 14"><circle cx="7" cy="4" r="1.6" fill="#fff"/><circle cx="13" cy="4" r="1.6" fill="#fff"/><path d="M4.5 11a2.5 2.5 0 0 1 5 0M10.5 11a2.5 2.5 0 0 1 5 0" stroke="#fff" stroke-width="1.3" fill="none"/></svg>Project Management</li>
    </ul>
  </div>

  <p class="tab">Affordable for small and large organizations</p>
  <div class="front-bar">
    <h2 class="front-headline">How <span class="accent">Prepared</span> Are You?</h2>
    <p class="standby">Stand-by<br><span class="accent">Contracts</span><br>Available</p>
  </div>
</section>

</body>
</html>
```